1 pg ad for national oil & gas publication

We need a fresh version of a draft ad we have for insertion in a national publication for oil and gas land service firms. The readers of the publication are other service firms and individuals and our clients - the in-house "landmen" at the oil and gas companies. Attached is what we drafted. We want something better, but definitely including our logo.

```html
<!DOCTYPE html>
<html lang="en">
<head>
<meta charset="utf-8">
<title>Ridgeline Land Services – Full Service Land Company</title>
<link rel="stylesheet" href="https://fonts.googleapis.com/css2?family=Open+Sans:ital,wght@1,400&family=Roboto+Condensed:wght@300;400;700&display=swap">
<style>
  :root {
    --gold: #c9a21a;
    --navy-top: #0b0b45;
    --navy-bottom: #26339c;
    --white: #ffffff;
    --yellow: #f2d21b;
    --tagline: #d9b21e;
    --green: #3fbf4a;
    --city-a: #1b2a6e;
    --city-b: #5b7fd0;
    --field-a: #c9cfd6;
    --field-b: #6e6a3a;
    --feature-light: #8fd4ff;
    --feature-mid: #2a78d6;
    --feature-deep: #16338f;
  }
  * { box-sizing: border-box; margin: 0; padding: 0; }
  html, body { width: 914px; height: 1200px; overflow: hidden; background: var(--gold); }
  .ad {
    position: relative;
    width: 914px; height: 1200px;
    border: 18px solid var(--gold);
    background: linear-gradient(180deg, var(--navy-top) 0%, #141a66 55%, var(--navy-bottom) 100%);
    font-family: "Roboto Condensed", Arial, sans-serif;
    font-weight: 300;
    color: var(--white);
    overflow: hidden;
  }
  .brand {
    position: absolute; left: 0; right: 0; top: 30px;
    text-align: center; line-height: 0.92;
    font-size: 74px; font-weight: 300; color: var(--white);
  }
  .tagline {
    position: absolute; left: 0; right: 0; top: 186px;
    text-align: center;
    font-family: "Open Sans", Arial, sans-serif; font-style: italic;
    font-size: 35px; color: var(--tagline);
  }
  .intro {
    position: absolute; left: 20px; right: 20px; top: 240px;
    text-align: center; font-size: 25px; line-height: 32px;
  }
  .positioning {
    position: absolute; left: 220px; right: 220px; top: 350px;
    text-align: center; font-size: 18px; line-height: 25px;
  }
  .photo { position: absolute; top: 395px; width: 170px; height: 158px; }
  .photo--city { left: 38px; background: linear-gradient(160deg, var(--city-a), var(--city-b) 60%, #2a2f55); }
  .photo--pump { right: 38px; background: linear-gradient(180deg, var(--field-a) 0%, #9da07a 55%, var(--field-b) 100%); }
  .services-heading {
    position: absolute; left: 0; right: 0; top: 498px;
    text-align: center; font-size: 28px; line-height: 32px; color: var(--yellow); font-weight: 400;
  }
  .feature-art {
    position: absolute; left: 295px; top: 566px; width: 270px; height: 452px;
    border-radius: 22px;
    background: radial-gradient(ellipse at 50% 60%, var(--feature-light) 0%, var(--feature-mid) 50%, var(--feature-deep) 100%);
  }
  .service-list { position: absolute; list-style: none; font-size: 23px; line-height: 25px; }
  .service-list li { position: absolute; width: 250px; }
  .service-list--left { left: 47px; top: 0; }
  .service-list--left li { left: 0; padding-left: 36px; }
  .service-list--right { right: 47px; top: 0; }
  .service-list--right li { right: 0; padding-right: 36px; text-align: right; }
  .service-list li::before {
    content: ""; position: absolute; top: 6px; width: 14px; height: 14px; background: var(--green);
  }
  .service-list--left li::before { left: 0; }
  .service-list--right li::before { right: 0; }
  .contacts {
    position: absolute; left: 0; right: 0; top: 1044px;
    display: flex; justify-content: center;
    font-size: 21.5px; line-height: 29.5px;
  }
  .contact { padding: 0 18px; width: 347px; }
  .contact--vp { text-align: right; border-right: 2px solid var(--white); }
  .contact--president { text-align: left; }
  .contact__name { font-weight: 700; }
</style>
</head>
<body>
<main class="ad">
  <h1 class="brand">Ridgeline Land<br>Services</h1>
  <p class="tagline">Expertly serving oil and gas stakeholders</p>
  <p class="intro">Ridgeline Land Services is a full-service consulting firm providing professional<br>land services to the oil and gas industry, attorneys, utilities, title insurers,<br>pipeline companies, developers, land owners and public agencies.</p>
  <p class="positioning">Our firm is uniquely positioned to assist with leasing,<br>permitting, acquisitions, divestitures, due diligence<br>and the day-to-day operational<br>challenges of drilling and producing in high<br>density urban environments throughout the Country.</p>

  <div class="photo photo--city" role="img" aria-label="Night city skyline with palm trees and light trails"></div>
  <div class="photo photo--pump" role="img" aria-label="Oil pump jack in a field"></div>

  <h2 class="services-heading">Ridgeline Land Services is a<br>Full Service Land Company providing:</h2>

  <div class="feature-art" role="img" aria-label="Water drop holding a globe and a city skyline"></div>

  <ul class="service-list service-list--left">
    <li style="top:626px">Oil, Gas &amp; Mineral<br>Consulting</li>
    <li style="top:687px">ARC/GIS Mapping</li>
    <li style="top:751px">Secure Online Maps</li>
    <li style="top:813px">Title Research</li>
    <li style="top:874px">Due Diligence</li>
    <li style="top:937px">Title Curative / Probate<br>Matters</li>
    <li style="top:996px">Seismic Permitting</li>
  </ul>
  <ul class="service-list service-list--right">
    <li style="top:623px">Leasing</li>
    <li style="top:668px">Surface and Mineral<br>Acquisitions</li>
    <li style="top:729px">Right-of-Way Title and<br>Acquisitions</li>
    <li style="top:794px">Permitting and<br>Regulatory Compliance</li>
    <li style="top:872px">Land&nbsp; Administration</li>
    <li style="top:936px">File Management</li>
    <li style="top:994px">Expert Witness</li>
  </ul>

  <section class="contacts">
    <div class="contact contact--vp">
      <p class="contact__name">DAN WHITFORD, RPL</p>
      <p>VICE PRESIDENT</p>
      <p>(337) 555-0142</p>
      <p>dwhitford@ridgelineland.com</p>
    </div>
    <div class="contact contact--president">
      <p class="contact__name">M. CLARE DUNMORE, Esq</p>
      <p>PRESIDENT</p>
      <p>(310) 555-0187</p>
      <p>cdunmore@ridgelineland.com</p>
    </div>
  </section>
</main>
</body>
</html>
```